Sticker label design for - Over Fleet Deodorant Balm

I need a label for my 100% Natural Deodorant Balm
The brand is called "Mild Meadow Brand", and the product is called OVER FLEET Deodorant Balm.
There are two labels, one is a 5.2cm circle for the top, and 4.5cm circle for the base. The jar is amber plastic with black lid.
Width: 5.8cm
Height: 3.4cm (Lid 1.2cm, base 2,2cm)
Here is a link to what the jar looks like from one of my competitors: https://redsparrow.com.au/products/body/crest-deodorant-paste/
The product is a unisex product. Please see uploaded files for designs previously made for the brand. I'm trying to see a few more designs before finalising my choice. Feel free to use the logo at the top (Mild Meadow Brand) of either attachment if you would like. Or design your own.
Be be aware that it is meant to be Aluminium and Paraben Free, not "Parabens" Weight of product is 70g, please include this.
Label can be any colour, and printed with regular colours or event gold, silver or rose gold foil. Would a background be nice?
This is something I saw that I liked:
http://www.tolvenbalm.com
However I'm really open to what people can come up with.
For the back base-
Over Fleet deodorant balm is made from 100% natural ingredients, and works by neutralises odour and minimising wetness without the use of harmful chemicals.
www.mildmeadowbrand.com
Directions: For optimal result, apply a pea size amount of the balm to your dry armpits. Gently rub the balm into your armpits covering the entire area. Discontinue use if irritation occurs.
Ingredients: Shea Butter, Coconut oil, Sodium Bicarbonate, Arrowroot, Kaolin Clay, Vitamin E, Vegetable Glycerin, Activated Charcoal, Essential oils of Peppermint, Lavender, Mandarin, Tea tree, Geranium Rose & Cedarwood.
MADE IN AUSTRALIA
Reason: Hi,
I'm not getting many submissions, so was hoping to extend the deadline.
Skin Care Product

```html
<!DOCTYPE html>
<html lang="en">
<head>
<meta charset="utf-8">
<title>Over Fleet Deodorant Balm – Lid Label</title>
<link href="https://fonts.googleapis.com/css2?family=Russo+One&family=Open+Sans:wght@600&family=Arimo:wght@400&display=swap" rel="stylesheet">
<style>
  :root {
    --page-bg: #ffffff;
    --label-cream: #fdf1c9;
    --label-cream-edge: #fbe7a8;
    --ink: #4a4450;
    --accent-orange: #f39a2a;
  }
  html, body {
    margin: 0;
    padding: 0;
    width: 1200px;
    height: 1200px;
    overflow: hidden;
    background: var(--page-bg);
  }
  .canvas {
    width: 1200px;
    height: 1200px;
    position: relative;
  }
  .lid-label {
    position: absolute;
    inset: 0;
  }
  .brand-arc-text {
    font-family: "Open Sans", sans-serif;
    font-weight: 600;
    font-size: 30px;
    letter-spacing: 9px;
    fill: var(--ink);
  }
  .product-name {
    font-family: "Russo One", sans-serif;
    font-size: 96px;
    fill: var(--ink);
  }
  .product-type {
    font-family: "Arimo", sans-serif;
    font-size: 46px;
    fill: var(--ink);
  }
</style>
</head>
<body>
<main class="canvas">
  <svg class="lid-label" viewBox="0 0 1200 1200" width="1200" height="1200">
    <defs>
      <radialGradient id="label-field" cx="50%" cy="50%" r="50%">
        <stop offset="0%" stop-color="var(--label-cream)"/>
        <stop offset="100%" stop-color="var(--label-cream-edge)"/>
      </radialGradient>
      <path id="brand-arc-path" d="M 324 471 A 305 305 0 0 1 876 471"/>
    </defs>

    <circle class="label-background" cx="600" cy="600" r="440" fill="url(#label-field)"
            role="img" aria-label="Soft cream tiled decorative background pattern"/>

    <path class="brand-arc-rule" d="M 336 493 A 285 285 0 0 1 864 493"
          fill="none" stroke="var(--accent-orange)" stroke-width="2.5"/>

    <text class="brand-arc-text" text-anchor="middle">
      <textPath href="#brand-arc-path" startOffset="50%">mild meadow brand</textPath>
    </text>

    <text class="product-name" x="600" y="627" text-anchor="middle"
          textLength="685" lengthAdjust="spacingAndGlyphs">OVER FLEET</text>

    <text class="product-type" x="600" y="691" text-anchor="middle"
          textLength="536" lengthAdjust="spacing">DEODORANT BALM</text>

    <path class="dotted-arc" d="M 305 731 A 333 333 0 0 0 895 731"
          fill="none" stroke="var(--ink)" stroke-width="7"
          stroke-linecap="round" stroke-dasharray="0 44"/>
  </svg>
</main>
</body>
</html>
```